Summit Builders Web Site / Business Cards

Construction Company that specializes in Water and Fire Damage, Residential ReModels, Landscaping and Building ADU (Accessory Dwelling Unit)

Growing and changing families often need additional space, and a remodeling project can often provide that. Adding a new area, or repurposing an existing one can satisfy this requirement.

Other times, homeowners want to update the look in their kitchen or bathroom with more than just a change of cabinetry or vanity doors and drawers. Whatever your needs are, Summit Builders has skilled workers who are bonded and insured, and ready to make your dreams and visions a reality.

Target Market(s)

Home Owners

Industry/Entity Type

Construction Company

Contact Information for Business Card

Center Logo with our information on the corners

Back side to be Logo Only
Contact Info
CSLB License # 4829516
info@summitbuildersca.example
www.summitbuildersca.example

Coding

Coded - Design and coding required

Number of Pages Required

5+ page

Font styles to use
Serif
Sans Serif

Requirements
Must have
• Using our Logo Colors
Home
About Us
Services
Projects / Portfolio
Contact Us
Nice to have
• Colors matching our Logo
Should not have
• Black because it doesnt match our logo

```html
<!DOCTYPE html>
<html lang="en">
<head>
<meta charset="utf-8">
<title>Summit Builders</title>
<link href="https://fonts.googleapis.com/css2?family=Playfair+Display:wght@400;700;900&family=Poppins:wght@300;400;500;600&display=swap" rel="stylesheet">
<style>
:root{
  --orange:#ff6a00;
  --peach:#e9a07f;
  --cream:#fff5f0;
  --dark:#222222;
  --footer:#1c1c1c;
  --ink:#1e1e1e;
  --muted:#8a8a8a;
  --light:#f4f4f4;
  --white:#ffffff;
  --serif:"Playfair Display", Georgia, serif;
  --sans:"Poppins", Arial, sans-serif;
}
*{margin:0;padding:0;box-sizing:border-box}
html,body{width:1200px;height:5146px;overflow:hidden}
body{position:relative;font-family:var(--sans);color:var(--ink);background:var(--white)}
.abs{position:absolute}
.photo{position:absolute}

/* header */
.site-header{position:absolute;left:0;top:0;width:1200px;height:90px;background:var(--white)}
.brand{position:absolute;left:134px;top:22px;display:flex;align-items:center;gap:8px}
.brand-mark{width:14px;height:14px;background:var(--orange)}
.brand-name{font-family:var(--sans);font-weight:600;font-size:17px;letter-spacing:1px;color:var(--ink);line-height:1.1}
.main-nav{position:absolute;top:40px;left:320px;display:flex;gap:0;font-size:12px;font-weight:500;letter-spacing:.5px}
.main-nav a{position:absolute;white-space:nowrap;color:var(--ink);text-decoration:none}
.main-nav a.active{color:var(--orange)}
.main-nav a.active::after{content:"";position:absolute;left:0;right:0;top:30px;height:2px;background:var(--orange)}
.nav-phone{color:var(--orange)!important}
.btn-quote{position:absolute;left:962px;top:30px;width:130px;height:36px;border:2px solid var(--orange);font-size:11px;font-weight:600;display:flex;align-items:center;justify-content:center;letter-spacing:.5px}

/* hero */
.hero{position:absolute;left:0;top:90px;width:1200px;height:642px;background:linear-gradient(180deg,#9eb0c6 0%,#c9d3de 35%,#6f86a6 65%,#3d5577 100%)}
.hero-accent{position:absolute;left:880px;top:90px;width:320px;height:642px;background:linear-gradient(180deg,rgba(233,160,127,.35),rgba(233,160,127,.75))}
.hero-title{position:absolute;left:0;width:1200px;top:306px;text-align:center;font-family:var(--serif);font-weight:700;font-size:66px;color:var(--white)}
.hero-sub{position:absolute;left:0;width:1200px;top:392px;text-align:center;font-family:var(--sans);font-weight:500;font-size:28px;letter-spacing:6px;color:var(--white)}
.btn-orange{position:absolute;background:var(--orange);color:var(--white);font-size:11px;font-weight:600;letter-spacing:.5px;display:flex;align-items:center;justify-content:center}
.hero-btn{left:538px;top:462px;width:146px;height:38px}

/* service cards */
.service-card{position:absolute;top:760px;width:368px;height:274px}
.service-card .label{position:absolute;left:26px;top:156px;width:320px;color:var(--white);font-weight:600;font-size:19px;letter-spacing:2px;line-height:22px;text-transform:uppercase}
.service-card .btn-orange{left:26px;top:216px;width:120px;height:30px;font-size:10px}

/* section experience */
.experience{position:absolute;left:0;top:1034px;width:1200px;height:766px;background:var(--cream)}
.rule{position:absolute;height:1px;background:#d9cfc9}
.heading-serif{position:absolute;font-family:var(--serif);font-weight:700;font-size:48px;line-height:56px;color:var(--ink)}
.heading-serif em{font-style:normal;color:var(--orange)}
.lead{position:absolute;font-size:13px;line-height:24px;color:#555}
.feature{position:absolute;width:280px}
.feature svg{display:block}
.feature h3{font-weight:500;font-size:17px;margin-top:16px;color:var(--ink)}
.feature p{font-size:11px;line-height:21px;color:var(--muted);margin-top:14px}

/* solutions */
.dark-band{position:absolute;left:0;top:2208px;width:1200px;height:852px}
.sub-title{position:absolute;font-weight:600;font-size:29px;color:var(--ink)}
.sub-title.light{color:var(--white)}
.body-text{position:absolute;font-size:13px;line-height:24px;color:#777}
.body-text.light{color:var(--white);font-weight:500}
.accent-line{position:absolute;background:var(--orange)}

/* stats */
.stat{position:absolute;top:3168px;width:214px;height:154px;background:var(--white);border-top:3px solid var(--peach);box-shadow:0 6px 16px rgba(0,0,0,.1)}
.stat .num{position:absolute;left:28px;top:22px;font-weight:300;font-size:44px;color:var(--orange)}
.stat .cap{position:absolute;left:28px;top:92px;font-family:var(--serif);font-weight:700;font-size:13px;line-height:16px;letter-spacing:1px;color:var(--ink);text-transform:uppercase}

/* testimonials */
.testi-heading{position:absolute;left:240px;top:3564px;font-family:var(--serif);font-weight:700;font-size:48px;line-height:56px;color:var(--white)}
.person{position:absolute;left:134px;display:flex;align-items:center}
.person .avatar{width:84px;height:84px;border-radius:50%;background:linear-gradient(135deg,#f3a06b,#e06018);flex:none}
.person .name{font-family:var(--serif);font-size:22px;color:var(--orange)}
.person .role{font-size:13px;color:var(--ink)}
.person.muted .name{color:#ffd3b3}
.person.muted .role{color:#ffd3b3}
.person.muted .avatar{background:linear-gradient(135deg,#ffd7bd,#f2a878)}
.quote-mark{position:absolute;left:586px;top:3590px;font-family:var(--serif);font-weight:900;font-size:90px;color:var(--orange);line-height:1}
.quote-text{position:absolute;left:586px;top:3688px;width:380px;font-size:18px;line-height:32px;color:#8a8a8a;font-weight:300}
.quote-name{position:absolute;left:586px;top:3932px;font-family:var(--serif);font-weight:700;font-size:22px;color:var(--orange)}
.quote-avatar{position:absolute;left:1016px;top:3700px;width:142px;height:142px;border-radius:50%;background:linear-gradient(135deg,#ff8a3a,#e95f00)}

/* blog */
.blog{position:absolute;left:0;top:4116px;width:1200px;height:644px;background:var(--light)}
.blog-title{position:absolute;left:0;width:1200px;top:4200px;text-align:center;font-family:var(--serif);font-weight:700;font-size:46px}
.post{position:absolute;top:4322px;width:306px;height:344px;background:var(--white);border-top:3px solid var(--orange);box-shadow:0 4px 12px rgba(0,0,0,.06)}
.post .thumb{position:absolute;left:0;top:0;width:306px;height:186px}
.post .date{position:absolute;left:28px;top:214px;font-size:10px;color:var(--orange);text-transform:uppercase;letter-spacing:.5px}
.post .title{position:absolute;left:28px;top:240px;width:260px;font-family:var(--serif);font-weight:700;font-size:13px;line-height:24px}
.post .arrow{position:absolute;left:28px;top:306px}

/* footer */
.site-footer{position:absolute;left:0;top:4760px;width:1200px;height:386px;background:var(--footer);color:#bdbdbd}
.site-footer h4{position:absolute;font-weight:500;font-size:15px;color:var(--white)}
.foot-text{position:absolute;font-size:11px;line-height:19px;color:#bdbdbd}
.foot-links{position:absolute;list-style:none;font-size:12px;line-height:29px;color:#bdbdbd}
.social{position:absolute;left:134px;top:142px;display:flex;gap:8px}
.social span{width:18px;height:18px;border:1px solid #bdbdbd;border-radius:50%}
.email-field{position:absolute;left:822px;top:206px;width:268px;height:40px;border:1px solid #555;font-size:11px;color:#bdbdbd;display:flex;align-items:center;padding-left:18px}
</style>
</head>
<body>

<header class="site-header">
  <div class="brand"><span class="brand-mark"></span><span class="brand-name">SUMMIT BUILDERS</span></div>
  <nav class="main-nav">
    <a class="active" style="left:0">HOME</a>
    <a style="left:82px">ABOUT US</a>
    <a style="left:184px">SERVICES</a>
    <a style="left:298px">PROJECTS</a>
    <a style="left:400px">CONTACT US</a>
    <a class="nav-phone" style="left:512px">+1 555 014 2290</a>
  </nav>
  <div class="btn-quote">GET A QUOTE</div>
</header>

<section>
  <div class="hero" role="img" aria-label="City skyline of glass towers under a cloudy sky"></div>
  <div class="hero-accent" role="img" aria-label="Peach architectural frame overlay"></div>
  <h1 class="hero-title">The Best Choose Us</h1>
  <p class="hero-sub">BECAUSE WE DELIVER</p>
  <div class="btn-orange hero-btn">CONTACT US</div>
  <svg class="abs" style="left:604px;top:636px" width="14" height="10" viewBox="0 0 14 10"><path d="M1 1l6 7 6-7" fill="none" stroke="#fff" stroke-width="1.5"/></svg>
</section>

<section>
  <article class="service-card" style="left:26px">
    <div class="photo" style="inset:0;background:linear-gradient(180deg,#d9d6d1,#8f8a84 60%,#5e5954)" role="img" aria-label="Living room with grey sofa after water damage"></div>
    <div class="label">Water and Fire<br>Damage</div>
    <div class="btn-orange">DISCOVER MORE</div>
  </article>
  <article class="service-card" style="left:416px">
    <div class="photo" style="inset:0;background:linear-gradient(180deg,#f1efea,#cfc9bf 55%,#5a4a3d)" role="img" aria-label="Bright remodeled white kitchen with wood floor"></div>
    <div class="label">Residential<br>Remodels</div>
    <div class="btn-orange">DISCOVER MORE</div>
  </article>
  <article class="service-card" style="left:806px">
    <div class="photo" style="inset:0;background:linear-gradient(180deg,#7a8e6a,#3f5b34 55%,#6c5747)" role="img" aria-label="Garden deck with trees beside an accessory dwelling unit"></div>
    <div class="label">Landscaping and<br>Building ADU</div>
    <div class="btn-orange">DISCOVER MORE</div>
  </article>
</section>

<section class="experience"></section>
<div class="rule" style="left:134px;top:1160px;width:80px"></div>
<h2 class="heading-serif" style="left:240px;top:1128px">Shaping A New<br><em>Experience</em></h2>
<p class="lead" style="left:668px;top:1140px;width:430px">Growing and changing families often need additional space, and a remodeling project can often provide that. Adding a new area, or repurposing an existing one can satisfy this requirement.</p>

<div class="feature" style="left:134px;top:1340px">
  <svg width="42" height="36" viewBox="0 0 42 36" fill="none" stroke="#ff6a00" stroke-width="2"><path d="M3 16L21 3l18 13"/><rect x="7" y="14" width="28" height="20"/><rect x="11" y="20" width="6" height="6"/><rect x="25" y="20" width="6" height="14"/></svg>
  <h3>Home Construction</h3>
  <p>We are rethoric question ran over her cheek When she reached the first hills of the Italic Mountains, she had a last view back</p>
</div>
<div class="feature" style="left:460px;top:1340px">
  <svg width="42" height="36" viewBox="0 0 42 36" fill="none" stroke="#ff6a00" stroke-width="2"><path d="M3 16L21 3l18 13"/><rect x="7" y="14" width="28" height="20"/><path d="M7 22h28M7 28h28M17 14v20M25 14v20"/></svg>
  <h3>Exterior Design</h3>
  <p>We are rethoric question ran over her cheek When she reached the first hills of the Italic Mountains, she had a last view back</p>
</div>
<div class="feature" style="left:786px;top:1340px">
  <svg width="42" height="36" viewBox="0 0 42 36" fill="none" stroke="#ff6a00" stroke-width="2"><path d="M5 16L21 3l16 13"/><rect x="9" y="14" width="24" height="20"/><rect x="16" y="18" width="10" height="8"/><path d="M9 30h24"/></svg>
  <h3>Building Remodeling</h3>
  <p>We are rethoric question ran over her cheek When she reached the first hills of the Italic Mountains, she had a last view back</p>
</div>
<div class="feature" style="left:134px;top:1540px">
  <svg width="42" height="40" viewBox="0 0 42 40" fill="none" stroke="#ff6a00" stroke-width="2"><path d="M3 18L21 3l18 15"/><path d="M8 14v22h26V14"/><circle cx="21" cy="24" r="6"/></svg>
  <h3>Renovation</h3>
  <p>We are rethoric question ran over her cheek When she reached the first hills of the Italic Mountains, she had a last view back</p>
</div>
<div class="feature" style="left:460px;top:1540px">
  <svg width="42" height="40" viewBox="0 0 42 40" fill="none" stroke="#ff6a00" stroke-width="2"><rect x="7" y="4" width="28" height="32"/><path d="M7 18h14V4M21 26h14M14 36V26"/></svg>
  <h3>Interior Design</h3>
  <p>We are rethoric question ran over her cheek When she reached the first hills of the Italic Mountains, she had a last view back</p>
</div>
<div class="feature" style="left:786px;top:1540px">
  <svg width="42" height="40" viewBox="0 0 42 40" fill="none" stroke="#ff6a00" stroke-width="2"><path d="M21 2l18 18-18 18L3 20z"/><path d="M13 20l8-8 8 8v8H13z"/></svg>
  <h3>Saftey Management</h3>
  <p>We are rethoric question ran over her cheek When she reached the first hills of the Italic Mountains, she had a last view back</p>
</div>

<!-- solutions -->
<svg class="dark-band" viewBox="0 0 1200 852" preserveAspectRatio="none"><polygon points="0,0 1200,0 1200,732 0,852" fill="#222222"/></svg>
<div class="rule" style="left:134px;top:1918px;width:80px"></div>
<h2 class="heading-serif" style="left:240px;top:1886px">Constructive<br>Solution You<br>Can <em>Trust</em></h2>

<h3 class="sub-title" style="left:692px;top:1904px">Kitchen or Bathroom</h3>
<p class="body-text" style="left:692px;top:1956px;width:370px">Growing and changing families often need additional space, and a remodeling project can often provide that. Adding a new area, or repurposing an existing one can satisfy this requirement.</p>
<div class="accent-line" style="left:714px;top:2078px;width:1px;height:34px"></div>
<div class="photo" style="left:692px;top:2110px;width:398px;height:256px;background:linear-gradient(160deg,#e8e6e3,#b9b5b0 60%,#7d7873)" role="img" aria-label="Bathroom vanity with double sinks and round mirrors"></div>

<div class="photo" style="left:0;top:2162px;width:600px;height:436px;background:linear-gradient(160deg,#7aa89a,#c08a45 45%,#7a4e22)" role="img" aria-label="Wooden kitchen island under pendant lights"></div>

<div class="accent-line" style="left:600px;top:2464px;width:66px;height:1px"></div>
<h3 class="sub-title light" style="left:692px;top:2446px">Doors and Drawers</h3>
<p class="body-text light" style="left:692px;top:2498px;width:370px">Growing and changing families often need additional space, and a remodeling project can often provide that. Adding a new area, or repurposing an existing one can satisfy this requirement.</p>

<h3 class="sub-title light" style="left:134px;top:2748px">Remodeling Project</h3>
<p class="body-text light" style="left:134px;top:2800px;width:370px">Growing and changing families often need additional space, and a remodeling project can often provide that. Adding a new area, or repurposing an existing one can satisfy this requirement.</p>
<div class="accent-line" style="left:564px;top:2766px;width:66px;height:1px"></div>
<div class="photo" style="left:588px;top:2730px;width:478px;height:306px;background:linear-gradient(160deg,#f2f2f2,#c8c8c8 55%,#8a8a8a)" role="img" aria-label="Modern remodeled living room with lounge chairs"></div>

<!-- stats -->
<div class="stat" style="left:134px"><div class="num">53</div><div class="cap">Total<br>Projects</div></div>
<div class="stat" style="left:382px"><div class="num">371</div><div class="cap">Staff<br>Members</div></div>
<div class="stat" style="left:628px"><div class="num">15</div><div class="cap">Working in<br>States</div></div>
<div class="stat" style="left:876px"><div class="num">2,600</div><div class="cap">Hours for<br>Work</div></div>

<!-- testimonials -->
<svg class="abs" style="left:0;top:3420px" width="532" height="696" viewBox="0 0 532 696"><polygon points="0,52 532,0 532,696 0,696" fill="#ff6a00"/></svg>
<div class="rule" style="left:134px;top:3566px;width:80px;background:#ffb27a"></div>
<h2 class="testi-heading">What<br>People Say<br>About Us</h2>
<div class="abs" style="left:134px;top:3762px;width:398px;height:108px;background:#fff;border-radius:54px 0 0 54px"></div>
<div class="person" style="top:3774px;left:146px"><div class="avatar" role="img" aria-label="Client portrait"></div><div style="margin-left:16px"><div class="name">Marisol Vance</div><div class="role">Business Developement</div></div></div>
<div class="person muted" style="top:3910px;left:146px"><div class="avatar" role="img" aria-label="Client portrait" style="width:84px;height:84px"></div><div style="margin-left:16px"><div class="name">Theo Brandt</div><div class="role">Business Developement</div></div></div>

<div class="quote-mark">&ldquo;</div>
<p class="quote-text">Lorem ipsum dolor sit amet, eius impetus et mel. Ubique facilisis has at. Usu ceteros voluptatum at, sea dicit euripidis reprimique ea. Id sea quaeque appareat voluptatibus, wisi splendide per cu. Purto maluisset disputationi cu eos.</p>
<div class="quote-name">Marisol Vance</div>
<div class="quote-avatar" role="img" aria-label="Client portrait on orange circle"></div>

<!-- blog -->
<section class="blog"></section>
<h2 class="blog-title">Blog Post</h2>
<div class="rule" style="left:574px;top:4276px;width:52px;background:#cfcfcf"></div>
<article class="post" style="left:134px">
  <div class="thumb" style="background:linear-gradient(160deg,#f3f3f3,#d9c4b8 60%,#b0413b)" role="img" aria-label="Person working at a desk in a bright office"></div>
  <div class="date">07 August 2020</div>
  <div class="title">Lorem ipsum dolor sit amet, eius impetus et mel. Ubique facilisis has at.</div>
  <svg class="arrow" width="14" height="8" viewBox="0 0 14 8"><path d="M0 4h12M9 1l3 3-3 3" fill="none" stroke="#ff6a00" stroke-width="1.4"/></svg>
</article>
<article class="post" style="left:460px">
  <div class="thumb" style="background:linear-gradient(160deg,#eeeeee,#9a9088 60%,#3e3530)" role="img" aria-label="Living room with shuttered windows"></div>
  <div class="date">07 August 2020</div>
  <div class="title">Lorem ipsum dolor sit amet, eius impetus et mel. Ubique facilisis has at.</div>
  <svg class="arrow" width="14" height="8" viewBox="0 0 14 8"><path d="M0 4h12M9 1l3 3-3 3" fill="none" stroke="#ff6a00" stroke-width="1.4"/></svg>
</article>
<article class="post" style="left:786px">
  <div class="thumb" style="background:radial-gradient(circle at 55% 45%,#d9b27a,#5a4632 45%,#1f1a15)" role="img" aria-label="Light falling into a dark rocky cave"></div>
  <div class="date">07 August 2020</div>
  <div class="title">Lorem ipsum dolor sit amet, eius impetus et mel. Ubique facilisis has at.</div>
  <svg class="arrow" width="14" height="8" viewBox="0 0 14 8"><path d="M0 4h12M9 1l3 3-3 3" fill="none" stroke="#ff6a00" stroke-width="1.4"/></svg>
</article>

<!-- footer -->
<footer class="site-footer">
  <div class="brand" style="top:96px"><span class="brand-mark"></span><span class="brand-name" style="color:#fff">SUMMIT BUILDERS</span></div>
  <div class="social"><span></span><span></span><span></span><span></span></div>
  <p class="foot-text" style="left:134px;top:222px">Daniel R Hale | Branch Manager</p>
  <p class="foot-text" style="left:134px;top:252px;width:200px">412 W Orchard Ave Fairview,<br>CA 90000</p>
  <p class="foot-text" style="left:134px;top:328px;letter-spacing:1px;color:#fff">©2020. SUMMIT BUILDERS</p>

  <h4 style="left:396px;top:96px">Contact Us</h4>
  <p class="foot-text" style="left:396px;top:136px">Office : 555-014-2290<br>Direct : 555-017-3348<br>Fax : 555-019-6624</p>
  <p class="foot-text" style="left:396px;top:226px;color:var(--orange)">dhale@summitbuildersca.example</p>

  <h4 style="left:636px;top:96px">Quick Link</h4>
  <ul class="foot-links" style="left:636px;top:130px"><li>Home</li><li>About Us</li><li>Service</li><li>Projects</li><li>Contact Us</li></ul>

  <h4 style="left:822px;top:96px">Be the first to know</h4>
  <p class="foot-text" style="left:822px;top:136px;width:270px">Lorem ipsum dolor sit amet, eius impetus et mel. Ubique facilisis has at. Usu ceteros voluptatum ates.</p>
  <div class="email-field">Email Address</div>
  <svg class="abs" style="left:1048px;top:220px" width="14" height="12" viewBox="0 0 14 12"><path d="M1 6l12-5-4 10-2-4z" fill="none" stroke="#ff6a00" stroke-width="1.3"/></svg>
</footer>

</body>
</html>
```